Calvanta Group Real Estate Company business cards

New business card design, we are generally happy with the basic layout of the existing front of business card, (feel free to change) but require a head shot photo on the back side.

http://www.calvanta.com.au/

Attached logos, and existing business card

------------------------------

Target Market(s)

Real estate

Industry/Entity Type

Real Estate

Contact Information for Business Card

Standard size double sided

Font styles to use
Other font styles liked:
• Futura

Requirements
Must have
• Photo head shot on the back side
Nice to have
• yes
Should not have
• No

```html
<!DOCTYPE html>
<html lang="en">
<head>
<meta charset="utf-8">
<title>Calvanta Group – Business Cards</title>
<link rel="stylesheet" href="https://fonts.googleapis.com/css2?family=Arimo:wght@400;700&display=swap">
<style>
  :root {
    --bg: #e7e6ea;
    --purple: #2f2160;
    --purple-soft: #3a2c70;
    --orange: #f7941d;
    --white: #ffffff;
    --photo-top: #4a4f6a;
    --photo-bottom: #262a45;
  }
  * { box-sizing: border-box; margin: 0; padding: 0; }
  html, body {
    width: 1200px; height: 1200px; overflow: hidden;
    background: var(--bg);
    font-family: "Arimo", Arial, sans-serif;
  }
  .canvas { position: relative; width: 1200px; height: 1200px; }
  .card {
    position: absolute; width: 640px; height: 390px;
    background: var(--purple); overflow: hidden;
    box-shadow: 0 10px 28px rgba(0,0,0,.22);
  }
  .card--front { left: 90px; top: 150px; }
  .card--back { left: 470px; top: 650px; }

  .wordmark {
    position: absolute; display: flex; align-items: center; gap: 10px;
    color: var(--white); font-size: 54px; font-weight: 400; letter-spacing: 1px;
    white-space: nowrap;
  }
  .wordmark__square { width: 12px; height: 12px; background: var(--orange); }
  .card--front .wordmark {
    left: 78px; top: 195px; transform: translate(-50%, -50%) rotate(-90deg);
  }
  .card--back .wordmark {
    left: 580px; top: 195px; transform: translate(-50%, -50%) rotate(90deg);
  }

  .arch { position: absolute; left: 0; top: 0; }
  .headshot {
    position: absolute; left: 440px; top: 34px; width: 170px; height: 356px;
    background: linear-gradient(180deg, var(--photo-top), var(--photo-bottom));
  }
  .tagline {
    position: absolute; left: 292px; top: 212px;
    color: var(--white); font-size: 22px; line-height: 1.35;
  }

  .details { position: absolute; left: 60px; top: 52px; color: var(--white); }
  .details__name { font-size: 28px; font-weight: 700; color: var(--orange); }
  .details__role { font-weight: 400; color: var(--white); }
  .details__company { margin-top: 22px; font-size: 23px; font-weight: 700; }
  .details__abn { font-size: 18px; }
  .contact { margin-top: 26px; list-style: none; font-size: 20px; line-height: 1.5; }
  .contact__label { color: var(--orange); margin-right: 6px; }
  .contact__value--bold { font-weight: 700; font-size: 22px; }
</style>
</head>
<body>
<main class="canvas">

  <section class="card card--front" aria-label="Card front">
    <svg class="arch" width="640" height="390" viewBox="0 0 640 390" aria-hidden="true">
      <path fill="var(--orange)" fill-rule="evenodd"
            d="M210 80 H560 V390 H210 Z M262 132 V390 H508 V132 Z"/>
    </svg>
    <div class="headshot" role="img" aria-label="Head shot of the director in a dark suit and blue tie"></div>
    <p class="tagline">let us<br>show you<br>property</p>
    <div class="wordmark"><span>calvanta</span><span class="wordmark__square"></span></div>
  </section>

  <section class="card card--back" aria-label="Card back">
    <div class="details">
      <p class="details__name">Daniel Tran <span class="details__role">| Director</span></p>
      <p class="details__company">Calvanta Group</p>
      <p class="details__abn">ABN: 12 345 678 901</p>
      <ul class="contact">
        <li><span class="contact__label">M:</span><span class="contact__value--bold">0400 555 218</span></li>
        <li><span class="contact__label">E:</span>daniel.tran@calvanta.com.au</li>
        <li><span class="contact__label">W:</span>www.calvanta.com.au</li>
      </ul>
    </div>
    <div class="wordmark"><span>calvanta</span><span class="wordmark__square"></span></div>
  </section>

</main>
</body>
</html>
```